Harrowgate Distillery Bottle Label Design

We need a label design for a product called "Cedar Lorne Straight Bourbon Whiskey". The bottle has two embossments on the side and an image printed on the back that will show through when looking from the front (shown in the attached image). It's made of 30% rye and 70% corn; images of the ingredients can be incorporated into the label design. We are a distillery that produces whiskey and bourbon from local farmers around the area. We focus on the quality of the ingredients and using the recipes passed down from generation to generation. We like a straight forward design using two colors maximum. The background will be brown once filled with the bourbon, so it must contrast against it (i.e. white and other lighter colors). The Harrowgate Distillery logo must be present on the bottle front, as well as 750 ml, 84 PROOF, 42% ALC/VOL.

Target Market(s)

Craft whiskey consumers.

Industry/Entity Type

Product

Colors
fee18a
fbe7d2
fff3d1
fefcee
fefdec
fdf9cf

Requirements
Must have
• 750 ml, 84 PROOF, 42% ALC/VOL. Aged for 3 years.The Harrowgate Distillery logo must be present on the bottle. Only two colors on label.
Nice to have
• Story of how we are a micro distillery making hand crafted whiskey.
Should not have
• False or misleading print.

```html
<!DOCTYPE html>
<html lang="en">
<head>
<meta charset="utf-8">
<title>Cedar Lorne Straight Bourbon Whiskey — Label</title>
<link rel="stylesheet" href="https://fonts.googleapis.com/css2?family=Playfair+Display:ital,wght@0,400;0,700;0,900;1,400;1,700&family=Pinyon+Script&family=Roboto+Condensed:wght@400;700&display=swap">
<style>
  :root {
    --backdrop: #2e2639;
    --label-gold: #f4d062;
    --label-gold-light: #f9e08f;
    --ink: #2a1d10;
    --ink-soft: #4a3620;
    --band-line: #a8854a;
    --paper-white: #fefcee;
  }
  * { margin: 0; padding: 0; box-sizing: border-box; }
  html, body {
    width: 1200px; height: 3172px; overflow: hidden;
    background: var(--backdrop);
  }
  .canvas {
    position: relative; width: 1200px; height: 3172px;
  }
  .label {
    position: absolute; left: 100px; top: 866px;
    width: 1000px; height: 1440px;
    background: linear-gradient(180deg, var(--label-gold-light) 0%, var(--label-gold) 55%, var(--label-gold-light) 100%);
    color: var(--ink);
    text-align: center;
    font-family: "Playfair Display", Georgia, serif;
  }
  .harvest-art {
    position: absolute; left: 295px; top: 150px;
    width: 410px; height: 430px;
    background: radial-gradient(ellipse at 50% 45%, var(--ink-soft) 0%, rgba(74,54,32,0.55) 45%, rgba(244,208,98,0) 72%);
  }
  .spec {
    position: absolute; top: 560px;
    font-family: "Roboto Condensed", Arial, sans-serif;
    font-size: 30px; color: var(--ink);
  }
  .spec--strength { left: 70px; }
  .spec--volume { right: 70px; font-size: 36px; }
  .product-origin {
    position: absolute; top: 628px; left: 0; right: 0;
    font-style: italic; font-size: 58px; color: var(--ink);
  }
  .name-band { position: absolute; left: 40px; right: 40px; top: 730px; height: 280px; }
  .name-band__tab {
    position: absolute; left: 200px; right: 200px; top: 0; height: 130px;
    background: var(--ink);
    border: 4px solid var(--band-line); border-bottom: none;
    font-style: italic; font-weight: 700; font-size: 96px; line-height: 126px;
    color: var(--label-gold);
  }
  .name-band__bar {
    position: absolute; left: 0; right: 0; top: 126px; height: 154px;
    background: var(--ink);
    border: 4px solid var(--band-line);
  }
  .name-band__rule {
    position: absolute; height: 6px; background: var(--band-line);
  }
  .name-band__word {
    position: absolute; left: 0; right: 0; top: 8px;
    font-weight: 900; font-size: 130px; line-height: 140px;
    letter-spacing: 10px; color: var(--paper-white);
  }
  .tagline {
    position: absolute; top: 1060px; left: 0; right: 0;
    font-family: "Pinyon Script", cursive;
    font-size: 98px; line-height: 96px; color: var(--ink);
  }
  .divider {
    position: absolute; top: 1280px; left: 60px; right: 60px;
    height: 3px; background: var(--ink);
  }
  .maker {
    position: absolute; top: 1298px; left: 0; right: 0;
    display: flex; align-items: center; justify-content: center; gap: 16px;
  }
  .maker__mark { width: 42px; height: 42px; border-radius: 50%; background: var(--ink); }
  .maker__name {
    font-family: "Roboto Condensed", Arial, sans-serif;
    font-weight: 700; font-size: 38px; color: var(--ink);
  }
  .maker__contact {
    position: absolute; top: 1356px; left: 0; right: 0;
    font-family: "Roboto Condensed", Arial, sans-serif;
    font-size: 22px; line-height: 28px; color: var(--ink);
  }
</style>
</head>
<body>
<main class="canvas">
  <section class="label">
    <div class="harvest-art" role="img" aria-label="Engraved illustration of an ear of corn flanked by rye stalks"></div>

    <p class="spec spec--strength">84 PF · 42% Alc / Vol</p>
    <p class="spec spec--volume">750ml.</p>

    <p class="product-origin">Cedar Lorne Straight</p>

    <div class="name-band">
      <div class="name-band__tab">Bourbon</div>
      <div class="name-band__bar">
        <span class="name-band__rule" style="left:20px; width:110px; top:50px;"></span>
        <span class="name-band__rule" style="left:20px; width:110px; top:90px;"></span>
        <span class="name-band__rule" style="right:20px; width:110px; top:50px;"></span>
        <span class="name-band__rule" style="right:20px; width:110px; top:90px;"></span>
        <span class="name-band__word">WHISKEY</span>
      </div>
    </div>

    <p class="tagline">Hand Crafted<br>Whiskey</p>

    <div class="divider"></div>

    <div class="maker">
      <span class="maker__mark"></span>
      <span class="maker__name">Harrowgate Distillery</span>
    </div>
    <p class="maker__contact">120 Mill Row, Harrowgate, MN 55000 · Tel: 555 010 2234<br>E-mail: hello@harrowgatedistillery.com</p>
  </section>
</main>
</body>
</html>
```